Dulwick Medical

Need smart and sleek business cards design for my medical distribution company. use logos attached.

add my details

Harriet Colbeck
Director/Sales Agent
harriet@dulwickmedical.com.au
0461 835 207

```html
<!DOCTYPE html>
<html lang="en">
<head>
<meta charset="utf-8">
<title>Dulwick Medical – Business Cards</title>
<link href="https://fonts.googleapis.com/css2?family=Montserrat:wght@600&family=Roboto+Condensed:wght@400;700&display=swap" rel="stylesheet">
<style>
  :root {
    --bg: #ced3d4;
    --paper: #f2f2f0;
    --navy: #141c5a;
    --navy-card: #0f1650;
    --blue: #2a8fd0;
    --ink: #2b2b2b;
    --white: #f4f4f4;
  }
  html, body {
    margin: 0;
    padding: 0;
    width: 1200px;
    height: 881px;
    overflow: hidden;
    background: var(--bg);
  }
  .stage {
    position: relative;
    width: 1200px;
    height: 881px;
  }
  .card {
    position: absolute;
    top: 298px;
    width: 500px;
    height: 286px;
    box-sizing: border-box;
    box-shadow: 0 14px 28px rgba(0,0,0,0.18);
  }
  .card--front {
    left: 68px;
    background: var(--paper);
    border-bottom: 3px solid var(--blue);
  }
  .card--back {
    left: 632px;
    background: var(--navy-card);
    border-bottom: 3px solid var(--blue);
    display: flex;
    align-items: center;
    justify-content: center;
  }
  .brand {
    position: absolute;
    left: 34px;
    top: 112px;
    width: 200px;
    display: flex;
    align-items: center;
    gap: 8px;
    font-family: "Montserrat", sans-serif;
    font-weight: 600;
    font-size: 21px;
    letter-spacing: 0.5px;
    color: var(--navy);
    line-height: 1.1;
  }
  .brand__mark {
    width: 14px;
    height: 14px;
    background: var(--navy);
    flex: none;
  }
  .divider {
    position: absolute;
    left: 246px;
    top: 70px;
    width: 2px;
    height: 146px;
    background: var(--blue);
  }
  .details {
    position: absolute;
    left: 268px;
    top: 78px;
    font-family: "Roboto Condensed", sans-serif;
    color: var(--ink);
  }
  .details__name {
    margin: 0;
    font-size: 25px;
    font-weight: 700;
    color: var(--navy);
    line-height: 1.1;
  }
  .details__name span { color: var(--blue); }
  .details__role {
    margin: 4px 0 18px;
    font-size: 14px;
  }
  .details__line {
    display: flex;
    align-items: center;
    gap: 7px;
    font-size: 14px;
    margin: 5px 0;
  }
  .details__line svg { width: 12px; height: 12px; flex: none; }
  .brand--large {
    position: static;
    width: auto;
    font-size: 40px;
    color: var(--white);
    gap: 14px;
  }
  .brand--large .brand__mark {
    width: 26px;
    height: 26px;
    background: var(--white);
  }
</style>
</head>
<body>
<main class="stage">
  <section class="card card--front" aria-label="Business card front">
    <div class="brand"><span class="brand__mark"></span>Dulwick Medical</div>
    <div class="divider"></div>
    <div class="details">
      <h1 class="details__name">Harriet <span>Colbeck</span></h1>
      <p class="details__role">Director/Sales Agent</p>
      <div class="details__line">
        <svg viewBox="0 0 12 12" aria-hidden="true"><path fill="#2a8fd0" d="M2.5 1l2 2.2-1 1.3c.6 1.4 1.6 2.4 3 3l1.3-1 2.2 2-1.2 2C4.6 10.2 1.8 7.4 1 3.2z"/></svg>
        0461 835 207
      </div>
      <div class="details__line">
        <svg viewBox="0 0 12 12" aria-hidden="true"><rect x="0.5" y="2" width="11" height="8" fill="#2a8fd0"/><path d="M0.5 2l5.5 4.5L11.5 2" fill="none" stroke="#f2f2f0" stroke-width="1"/></svg>
        harriet@dulwickmedical.com.au
      </div>
    </div>
  </section>

  <section class="card card--back" aria-label="Business card back">
    <div class="brand brand--large"><span class="brand__mark"></span>Dulwick Medical</div>
  </section>
</main>
</body>
</html>
```